Veteran Owned General Contractor needs Bold New Business Cards

We are a service disabled veteran owned small business. We're a general contractor that specializes in excavation, underground utilities, site work, land clearing and demolition. We would like a fresh, simple, bold, new look for our business cards. We're open to ideas! We'd like to incorporate the following information on the card:

Company Name & Logo, Name of Person, Job Title, Office Phone, Fax, Cell Phone, Email Address, Website, SDVOSB

Our logo is included. We look forward to your thoughts.

Thank you!
Updates

Reason: Hello Due to the overwhelming response to this project, we are extending the deadline one time to allow for improved communication and feedback with the top candidates. We would like to thank everyone for their hard work and exceptional creativity! Thank you

Industry/Entity Type

Business

Contact Information for Business Card

Font styles to use
Sans Serif

Requirements
Nice to have
• As we are a veteran owned company, it would be nice to incorporate an American flag into the design. Maybe on the back?

```html
<!DOCTYPE html>
<html lang="en">
<head>
<meta charset="utf-8">
<title>Keystone 4 Inc – Business Cards</title>
<link href="https://fonts.googleapis.com/css2?family=Michroma&display=swap" rel="stylesheet">
<style>
  :root {
    --backdrop: #262626;
    --card-edge: #0c0c0c;
    --card-glow: #3a3a3a;
    --brand-green: #74c043;
    --muted-grey: #8a8a8a;
    --mark-grey: #4a4a4a;
  }
  * { margin: 0; padding: 0; box-sizing: border-box; }
  html, body {
    width: 1200px;
    height: 1200px;
    overflow: hidden;
    background: var(--backdrop);
    font-family: "Michroma", sans-serif;
  }
  .business-card {
    position: absolute;
    top: 240px;
    width: 420px;
    height: 720px;
    overflow: hidden;
    box-shadow: 0 20px 50px rgba(0,0,0,.5);
  }
  .business-card--front { left: 150px; }
  .business-card--back { left: 630px; }

  .card-face {
    position: absolute;
    left: 50%;
    top: 50%;
    width: 720px;
    height: 420px;
    transform: translate(-50%, -50%) rotate(90deg);
    background: radial-gradient(ellipse at 50% 55%, var(--card-glow) 0%, #1c1c1c 45%, var(--card-edge) 100%);
  }
  .accent-band {
    position: absolute;
    top: 0;
    height: 100%;
    background: var(--brand-green);
  }
  .accent-band--wide { left: 0; width: 66px; }
  .accent-band--thin { right: 0; width: 16px; }

  .brand-lockup {
    position: absolute;
    display: flex;
    align-items: center;
    gap: 18px;
  }
  .brand-mark {
    width: 44px;
    height: 44px;
    background: var(--mark-grey);
    border-radius: 6px;
  }
  .brand-name {
    color: var(--brand-green);
    font-size: 34px;
    letter-spacing: 4px;
    line-height: 1;
  }
  .business-card--front .brand-lockup { left: 130px; top: 70px; }
  .business-card--back .brand-lockup { left: 150px; top: 168px; }

  .contact-block {
    position: absolute;
    left: 300px;
    top: 210px;
    color: var(--brand-green);
  }
  .person-name { font-size: 21px; letter-spacing: 1px; }
  .person-title { font-size: 11px; color: var(--brand-green); margin: 4px 0 14px; }
  .contact-row {
    display: flex;
    align-items: flex-start;
    gap: 12px;
    font-size: 13px;
    line-height: 1.55;
  }
  .contact-icon {
    width: 16px;
    height: 16px;
    margin-top: 3px;
    flex-shrink: 0;
  }
  .website-line {
    position: absolute;
    left: 150px;
    top: 118px;
    font-size: 11px;
    letter-spacing: 3px;
    color: var(--muted-grey);
  }
</style>
</head>
<body>

<section class="business-card business-card--front">
  <div class="card-face">
    <div class="accent-band accent-band--wide"></div>
    <div class="accent-band accent-band--thin"></div>

    <div class="brand-lockup">
      <span class="brand-mark"></span>
      <span class="brand-name">KEYSTONE 4</span>
    </div>

    <div class="contact-block">
      <p class="person-name">Dalton Reece</p>
      <p class="person-title">Owner</p>

      <div class="contact-row">
        <svg class="contact-icon" viewBox="0 0 16 16" fill="none" stroke="currentColor" stroke-width="1.4">
          <path d="M8 15s5-5 5-9a5 5 0 0 0-10 0c0 4 5 9 5 9z"/><circle cx="8" cy="6" r="1.8"/>
        </svg>
        <p>4820 NE 77th Ct<br>Ridgefield, WA 98642</p>
      </div>
      <div class="contact-row">
        <svg class="contact-icon" viewBox="0 0 16 16" fill="none" stroke="currentColor" stroke-width="1.4">
          <circle cx="8" cy="8" r="7"/><path d="M5.5 4.5l1.5 2-1 1a5 5 0 0 0 2.5 2.5l1-1 2 1.5-1 1.5c-3 0-6-3-6-6z"/>
        </svg>
        <p>360.555.0148</p>
      </div>
      <div class="contact-row">
        <svg class="contact-icon" viewBox="0 0 16 16" fill="none" stroke="currentColor" stroke-width="1.4">
          <circle cx="8" cy="8" r="7"/><rect x="4" y="5.5" width="8" height="5"/><path d="M4 5.5l4 3 4-3"/>
        </svg>
        <p>office@keystone4inc.com</p>
      </div>
      <div class="contact-row">
        <svg class="contact-icon" viewBox="0 0 16 16" fill="none" stroke="currentColor" stroke-width="1.4">
          <circle cx="8" cy="8" r="7"/><ellipse cx="8" cy="8" rx="3" ry="7"/><path d="M1 8h14"/>
        </svg>
        <p>www.keystone4inc.com</p>
      </div>
    </div>
  </div>
</section>

<section class="business-card business-card--back">
  <div class="card-face">
    <div class="accent-band accent-band--wide"></div>
    <div class="accent-band accent-band--thin"></div>

    <p class="website-line">www.keystone4inc.com</p>
    <div class="brand-lockup">
      <span class="brand-mark"></span>
      <span class="brand-name">KEYSTONE 4</span>
    </div>
  </div>
</section>

</body>
</html>
```